Solar Billboard Design

We require a billboard 24ftx10ft in size for our solar company.
Artwork Requirement’s:
• Sent on PDF file
• At least 300 dpi
• Scaled to 25% of banner size (24ft x 10ft)
• Please allow at least 40mm space from the artwork edge to allow for any hems and eyelets. This will ensure any important text/images are not cropped/overlapped.
The billboard must have on it:
Solar & Battery Packages
From £8750
In Stock Now!
brightfieldpower.co.uk (must stand out)
________________________
I have attached our logo and some images. I'm not sure if they are good enough quality so you may need to use a stock image.
Kind regards,
Marcus
Target Market(s)
Men & Women aged 35-70, homeowners
Industry/Entity Type
Solar / Construction
Look and feel
Each slider illustrates characteristics of the customer's brand and the style your logo design should communicate.

```html
<!DOCTYPE html>
<html lang="en">
<head>
<meta charset="UTF-8">
<title>Solar &amp; Battery Packages Billboard</title>
<link rel="stylesheet" href="https://fonts.googleapis.com/css2?family=Bebas+Neue&family=Open+Sans:wght@400;700;800&family=Montserrat:wght@500&display=swap">
<style>
  :root {
    --green: #2ecc64;
    --charcoal: #4a4a4a;
    --ink: #111111;
    --white: #ffffff;
    --stage: #e9edf1;
    --roof: #d9743f;
    --panel: #2c3a63;
    --wall: #efe4d2;
  }
  * { margin: 0; padding: 0; box-sizing: border-box; }
  html, body {
    width: 1200px;
    height: 756px;
    overflow: hidden;
    background: var(--stage);
  }
  .billboard {
    position: absolute;
    left: 24px;
    top: 128px;
    width: 1152px;
    height: 500px;
    background: var(--white);
    overflow: hidden;
  }
  .green-band {
    position: absolute;
    inset: 0;
    width: 100%;
    height: 100%;
  }
  .house-photo {
    position: absolute;
    left: 417px;
    top: 186px;
    width: 683px;
    height: 314px;
    background: linear-gradient(180deg, var(--roof) 0%, var(--panel) 30%, var(--panel) 48%, var(--roof) 60%, var(--wall) 72%, var(--wall) 100%);
  }
  .headline {
    position: absolute;
    left: 46px;
    top: 32px;
    font-family: "Open Sans", Arial, sans-serif;
    font-weight: 800;
    font-size: 66px;
    line-height: 73px;
    letter-spacing: -1px;
  }
  .headline span { display: block; }
  .headline .accent { color: var(--green); }
  .headline .dark { color: var(--charcoal); }
  .web-pill {
    position: absolute;
    left: 388px;
    top: 48px;
    width: 415px;
    height: 62px;
    border: 1.5px solid var(--ink);
    border-radius: 31px;
    display: flex;
    align-items: center;
    justify-content: center;
    font-family: "Open Sans", Arial, sans-serif;
    font-weight: 700;
    font-size: 25px;
    color: var(--ink);
    letter-spacing: -0.3px;
  }
  .brand {
    position: absolute;
    left: 838px;
    top: 54px;
    display: flex;
    align-items: center;
    gap: 14px;
  }
  .brand-mark {
    width: 70px;
    height: 70px;
    background: var(--green);
    flex: none;
  }
  .brand-name {
    font-family: "Montserrat", Arial, sans-serif;
    font-weight: 500;
    font-size: 21px;
    line-height: 34px;
    letter-spacing: 4px;
    color: var(--charcoal);
    text-transform: uppercase;
  }
  .price {
    position: absolute;
    left: 44px;
    top: 370px;
    font-family: "Bebas Neue", Impact, sans-serif;
    font-size: 80px;
    line-height: 76px;
    color: var(--white);
  }
  .stock {
    position: absolute;
    left: 44px;
    top: 440px;
    font-family: "Open Sans", Arial, sans-serif;
    font-weight: 800;
    font-size: 41px;
    line-height: 48px;
    letter-spacing: -1.5px;
    color: var(--charcoal);
  }
</style>
</head>
<body>
  <main class="billboard">
    <svg class="green-band" viewBox="0 0 1152 500" aria-hidden="true">
      <polygon points="0,355 1152,138 1152,500 0,500" fill="var(--green)"/>
    </svg>

    <div class="house-photo" role="img" aria-label="Photo of a house with a terracotta tiled roof fitted with two rows of solar panels"></div>

    <h1 class="headline">
      <span class="accent">SOLAR &amp;</span>
      <span class="accent">BATTERY</span>
      <span class="dark">PACKAGES</span>
    </h1>

    <div class="web-pill">www.brightfieldpower.co.uk</div>

    <div class="brand">
      <div class="brand-mark"></div>
      <div class="brand-name">Brightfield<br>Power<br>Group</div>
    </div>

    <p class="price">FROM £8750</p>
    <p class="stock">IN STOCK NOW!</p>
  </main>
</body>
</html>
```